"Bel Amora" Wholesale Box Design

We are a wholesale fruit distributing company and we have to create our own cherry packaging design.
These cherries are from Canada, and will be exported to several countries. They must accentuate the premium quality we are packing!
This box must work well for our customers all over the world (North America, Asia, Middle East, Europe, etc).
We prefer a cartoon-ish style, similar to our other labels.
Go crazy, make it as wild or as conservative as you want. Let's see what you can come up with!

Target Market(s)

Fruit importers and supermarkets.
Asian, Middle Eastern, European customers.

Industry/Entity Type

Wholesale

Colors

Designer to choose colors to be used in the design.

Requirements
Must have
• Style similar to our other labels (examples attached).
• It must include the following, as seen in the attached sample box:
• - PRODUCT OF CANADA
• - PRODUIT DU CANADA
• - CATEGORY No. 1
• - 5kg - 11lb
• It must include our logo (see attached), and show the following text:
• - Distributed by: Quilby Traders, Dunmore Falls, NV 89071 USA
• - www.quilbytraders.example
• It must be maximum 3 colors (and/or a combination of them).
Nice to have
• Would like to see a feminine looking cherry. "Bel Amora" means "My Dear" in French, but also sounds like a "My Cherry".

```html
<!DOCTYPE html>
<html lang="en">
<head>
<meta charset="utf-8">
<title>Bel Amora – Cherry Box Dieline</title>
<link href="https://fonts.googleapis.com/css2?family=Dancing+Script:wght@700&family=Open+Sans:wght@600;700;800&family=Libre+Baskerville&display=swap" rel="stylesheet">
<style>
  :root{
    --paper:#ebebeb;
    --blush:#f27f7f;
    --cherry:#be1622;
    --white:#ffffff;
    --leaf:#3a9a3a;
    --logo-green:#8cc63f;
    --dieline:#1a8fd6;
    --ink:#111111;
  }
  html,body{margin:0;padding:0;width:1200px;height:1076px;overflow:hidden;background:var(--paper);}
  .box-net{display:block;width:1200px;height:1076px;}
  .panel{fill:var(--blush);}
  .ribbon{fill:var(--cherry);}
  .cut-line{fill:none;stroke:var(--dieline);stroke-width:5;}
  .fold-line{fill:none;stroke:var(--dieline);stroke-width:6;stroke-dasharray:34 10 8 10;}
  .handle{fill:none;stroke:var(--dieline);stroke-width:5;}
  .brand-script{font-family:"Dancing Script",cursive;font-weight:700;fill:var(--cherry);}
  .brand-script.on-flap{stroke:var(--white);stroke-width:1.2;paint-order:stroke;}
  .logo-name{font-family:"Open Sans",sans-serif;font-weight:700;font-size:20px;fill:var(--logo-green);}
  .logo-dot{fill:var(--logo-green);}
  .info{font-family:"Open Sans",sans-serif;font-weight:700;fill:var(--ink);font-size:13px;}
  .info-grade{font-family:"Open Sans",sans-serif;font-weight:800;fill:var(--ink);font-size:20px;}
  .info-weight{font-family:"Open Sans",sans-serif;font-weight:800;fill:var(--ink);font-size:30px;}
  .badge-ring{fill:var(--white);}
  .badge-text{font-family:"Libre Baskerville",serif;font-size:12px;fill:var(--ink);letter-spacing:1px;}
  .flag-band{fill:#ff0000;}
  .flag-field{fill:var(--white);}
  .art-cherries{fill:var(--cherry);}
  .label-frame{fill:var(--cherry);}
  .label-face{fill:var(--white);}
</style>
</head>
<body>
<svg class="box-net" viewBox="0 0 1316 1180" preserveAspectRatio="none" xmlns="http://www.w3.org/2000/svg">
  <defs>
    <linearGradient id="cherry-art" x1="0" y1="0" x2="0" y2="1">
      <stop offset="0" stop-color="#3a9a3a"/>
      <stop offset="0.45" stop-color="#3a9a3a"/>
      <stop offset="0.55" stop-color="#d42a32"/>
      <stop offset="1" stop-color="#be1622"/>
    </linearGradient>
    <path id="ring-top" d="M -62 0 A 62 62 0 0 1 62 0"/>
    <path id="ring-bottom" d="M -71 0 A 71 71 0 0 0 71 0"/>
    <clipPath id="flag-clip"><circle r="56"/></clipPath>
  </defs>

  <!-- panels -->
  <rect class="panel" x="63" y="82" width="1177" height="186"/>
  <rect class="panel" x="63" y="283" width="1177" height="607"/>
  <rect class="panel" x="63" y="908" width="1177" height="182"/>
  <rect class="panel" x="258" y="262" width="785" height="646"/>

  <!-- ribbon -->
  <rect class="ribbon" x="578" y="268" width="62" height="630"/>
  <rect class="ribbon" x="258" y="555" width="795" height="63"/>

  <!-- cut lines -->
  <path class="cut-line" d="M63 265 V82 H1240 V265 M63 265 H258 M1043 265 H1240"/>
  <path class="cut-line" d="M63 890 V283 H248 L258 272 M1240 890 V283 H1053 L1043 272 M63 890 H248 L258 898 M1240 890 H1053 L1043 898"/>
  <path class="cut-line" d="M63 1108 V908 H258 M1240 1108 V908 H1043 M63 1090 H1240"/>
  <!-- fold lines -->
  <path class="fold-line" d="M258 270 H1043 M258 900 H1043 M258 270 V900 M1043 88 V1108"/>

  <!-- handles and slots -->
  <path class="handle" d="M470 270 V236 Q470 222 484 222 H606 Q620 222 620 236 V270"/>
  <path class="handle" d="M683 270 V236 Q683 222 697 222 H819 Q833 222 833 236 V270"/>
  <path class="handle" d="M470 900 V936 Q470 950 484 950 H606 Q620 950 620 936 V900"/>
  <path class="handle" d="M683 900 V936 Q683 950 697 950 H819 Q833 950 833 936 V900"/>
  <path class="handle" d="M256 367 H281 Q297 367 297 383 V424 Q297 440 281 440 H256"/>
  <path class="handle" d="M256 733 H281 Q297 733 297 749 V790 Q297 806 281 806 H256"/>
  <path class="handle" d="M1047 367 H1021 Q1005 367 1005 383 V424 Q1005 440 1021 440 H1047"/>
  <path class="handle" d="M1047 733 H1021 Q1005 733 1005 749 V790 Q1005 806 1021 806 H1047"/>
  <rect class="handle" x="1086" y="488" width="94" height="198" rx="6"/>

  <!-- top flap (upside down) -->
  <g class="flap-top" transform="rotate(180 658 170)">
    <text class="brand-script on-flap" x="720" y="236" font-size="100" text-anchor="middle">Bel Amora</text>
    <rect class="art-cherries" x="286" y="90" width="112" height="145" rx="30" fill="url(#cherry-art)" role="img" aria-label="Illustration of two cherries on a curling stem"/>
    <g class="logo">
      <circle class="logo-dot" cx="925" cy="112" r="14"/>
      <text class="logo-name" x="944" y="120">Quilby Traders</text>
    </g>
  </g>

  <!-- bottom flap -->
  <g class="flap-bottom">
    <rect x="290" y="918" width="110" height="142" rx="30" fill="url(#cherry-art)" role="img" aria-label="Illustration of two cherries on a curling stem"/>
    <text class="brand-script on-flap" x="690" y="1052" font-size="104" text-anchor="middle">Bel Amora</text>
    <g class="logo">
      <circle class="logo-dot" cx="900" cy="940" r="12"/>
      <text class="logo-name" x="916" y="947" font-size="18">Quilby Traders</text>
    </g>
  </g>

  <!-- central label -->
  <g class="main-label">
    <path class="label-frame" d="M380 415 H820 Q835 440 855 445 V715 Q835 720 820 745 H380 Q365 720 345 715 V445 Q365 440 380 415 Z"/>
    <path class="label-face" d="M388 428 H812 Q826 450 842 455 V705 Q826 710 812 732 H388 Q374 710 358 705 V455 Q374 450 388 428 Z"/>
    <rect x="390" y="445" width="160" height="210" rx="40" fill="url(#cherry-art)" role="img" aria-label="Illustration of two glossy cherries on a heart-shaped curling stem"/>
    <g class="logo">
      <circle class="logo-dot" cx="570" cy="478" r="13"/>
      <text class="logo-name" x="588" y="486">Quilby Traders</text>
    </g>
    <text class="brand-script" x="695" y="590" font-size="100" text-anchor="middle">Bel</text>
    <text class="brand-script" x="680" y="702" font-size="92" text-anchor="middle">Amora</text>
  </g>

  <!-- left side panel -->
  <g class="origin-badge" transform="translate(156 440) rotate(90)">
    <circle class="badge-ring" r="78"/>
    <g clip-path="url(#flag-clip)">
      <rect class="flag-field" x="-56" y="-56" width="112" height="112"/>
      <rect class="flag-band" x="-56" y="-56" width="30" height="112"/>
      <rect class="flag-band" x="26" y="-56" width="30" height="112"/>
    </g>
    <rect class="flag-band" x="-14" y="-16" width="28" height="30" role="img" aria-label="Maple leaf emblem"/>
    <text class="badge-text" text-anchor="middle"><textPath href="#ring-top" startOffset="50%">PRODUCT OF CANADA</textPath></text>
    <text class="badge-text" text-anchor="middle"><textPath href="#ring-bottom" startOffset="50%">PRODUIT DU CANADA</textPath></text>
  </g>
  <g class="shipping-info" transform="translate(0 642) rotate(90)">
    <text class="info" x="0" y="-220">Distributed by:</text>
    <text class="info" x="0" y="-200">Quilby Traders</text>
    <text class="info" x="0" y="-180">Dunmore Falls, NV 89071 USA</text>
    <text class="info" x="0" y="-160">www.quilbytraders.example</text>
    <text class="info-grade" x="0" y="-128">CATEGORY No. 1</text>
    <text class="info-weight" x="0" y="-84">5kg - 11lb</text>
  </g>

  <!-- right side panel -->
  <g class="origin-badge" transform="translate(1142 790) rotate(-90)">
    <circle class="badge-ring" r="80"/>
    <g clip-path="url(#flag-clip)">
      <rect class="flag-field" x="-56" y="-56" width="112" height="112"/>
      <rect class="flag-band" x="-56" y="-56" width="30" height="112"/>
      <rect class="flag-band" x="26" y="-56" width="30" height="112"/>
    </g>
    <rect class="flag-band" x="-14" y="-16" width="28" height="30" role="img" aria-label="Maple leaf emblem"/>
    <text class="badge-text" text-anchor="middle"><textPath href="#ring-top" startOffset="50%">PRODUCT OF CANADA</textPath></text>
    <text class="badge-text" text-anchor="middle"><textPath href="#ring-bottom" startOffset="50%">PRODUIT DU CANADA</textPath></text>
  </g>
  <g class="shipping-info" transform="translate(0 470) rotate(-90)">
    <text class="info" x="0" y="1080">Distributed by:</text>
    <text class="info" x="0" y="1100">Quilby Traders</text>
    <text class="info" x="0" y="1120">Dunmore Falls, NV 89071 USA</text>
    <text class="info" x="0" y="1140">www.quilbytraders.example</text>
    <text class="info-grade" x="0" y="1172">CATEGORY No. 1</text>
    <text class="info-weight" x="0" y="1216">5kg - 11lb</text>
  </g>
</svg>
</body>
</html>
```